Business Card Design Project

I am a psychotherapist, counselor and expressive arts therapist (means I use every art form imaginable in the service of healing). I'm just starting out in private practice in San Francisco, CA. I work with individual adults, children and families. I'd like the card to mirror the simplicity and color palate of my website. I also would love if there is a symbol, image of fire, flame or spark (that is warming, not frightening).

Check out my website: www.lorabecketmft.com

I want the cards to be printed in letter press so please keep that in mind!

Target Market(s)

Upper Middle Class Adults who are progressively minded, artistic or artists, open to psychotherapy, interested in health & healing.

Industry/Entity Type

Business

Requirements
Must have
• Text to be included:

Lora Becket
Counseling, Psychotherapy & Expressive Arts

2914 Alderwood Avenue, Suite D
San Francisco, CA 94127
p. 415.206.3791
lorajanebecket@meadowpost.net

www.lorabecketmft.com

MFT License Number 48671

It's OK to abbreviate Number to # or Street to St., etc.

Must be compatible with letter press printing.
Nice to have
• I don't have a logo. I don't expect designers to necessarily create one for me, but if someone comes up with a simple image (see above about flame), that would be great. I don't have much of a budget now, but expect that to change in the next year or so and then could buy a logo for my website, future letterhead, etc.

```html
<!DOCTYPE html>
<html lang="en">
<head>
<meta charset="utf-8">
<title>Lora Becket — Business Card</title>
<link rel="stylesheet" href="https://fonts.googleapis.com/css2?family=Libre+Baskerville:wght@400;700&display=swap">
<style>
  :root {
    --page: #dcdcdc;
    --card: #f4f4f2;
    --red: #d3171c;
    --ink: #4a4a4a;
    --ink-soft: #5c5c5c;
    --flame: #f2d21a;
  }
  * { box-sizing: border-box; margin: 0; padding: 0; }
  html, body { width: 1200px; height: 1200px; overflow: hidden; }
  body {
    background: var(--page);
    font-family: "Libre Baskerville", Georgia, serif;
    position: relative;
  }
  .card {
    position: absolute;
    left: 250px;
    width: 700px;
    height: 400px;
    background: var(--card);
    box-shadow: 0 2px 10px rgba(0,0,0,0.12);
  }
  .card-front { top: 150px; }
  .card-back { top: 650px; }

  /* Front */
  .brand-name {
    position: absolute;
    left: 290px;
    top: 120px;
    color: var(--red);
    font-size: 30px;
    font-variant: small-caps;
    letter-spacing: 1px;
  }
  .brand-mark {
    position: absolute;
    left: 120px;
    top: 196px;
    width: 26px;
    height: 26px;
    border-radius: 50%;
    background: var(--flame);
  }
  .services {
    position: absolute;
    left: 165px;
    top: 186px;
    list-style: none;
  }
  .services li {
    color: var(--ink-soft);
    font-size: 18px;
    line-height: 26px;
    padding-left: 10px;
    border-left: 2px solid var(--red);
    margin-bottom: 2px;
  }

  /* Back */
  .holder-name {
    position: absolute;
    left: 44px;
    top: 38px;
    color: var(--ink);
    font-size: 26px;
    font-weight: 700;
  }
  .licence {
    position: absolute;
    left: 44px;
    top: 80px;
    color: var(--ink-soft);
    font-size: 16px;
    padding-left: 10px;
    border-left: 2px solid var(--red);
  }
  .divider {
    position: absolute;
    left: 0;
    top: 210px;
    width: 620px;
    height: 4px;
  }
  .contact {
    position: absolute;
    left: 44px;
    top: 240px;
    width: 630px;
    color: var(--ink);
    font-size: 17px;
    line-height: 30px;
  }
  .contact-row { display: flex; white-space: nowrap; }
  .contact-row .cell { min-width: 290px; }
  .label { color: var(--red); font-weight: 700; margin-right: 6px; }
</style>
</head>
<body>
  <section class="card card-front">
    <h1 class="brand-name">Lora Becket</h1>
    <span class="brand-mark"></span>
    <ul class="services">
      <li>Counseling</li>
      <li>Psychotherapy</li>
      <li>Expressive Arts</li>
    </ul>
  </section>

  <section class="card card-back">
    <h2 class="holder-name">Lora Becket</h2>
    <p class="licence">MFT License #48671</p>
    <svg class="divider" viewBox="0 0 620 4" preserveAspectRatio="none" aria-hidden="true">
      <defs>
        <linearGradient id="divider-fade" x1="0" x2="1" y1="0" y2="0">
          <stop offset="0" stop-color="#d3171c"/>
          <stop offset="0.75" stop-color="#d3171c"/>
          <stop offset="1" stop-color="#e86a2a" stop-opacity="0"/>
        </linearGradient>
      </defs>
      <rect width="620" height="4" fill="url(#divider-fade)"/>
    </svg>
    <div class="contact">
      <div class="contact-row"><span class="label">a:</span>2914 Alderwood Avenue, Suite D, San Francisco, CA 94127</div>
      <div class="contact-row">
        <span class="cell"><span class="label">f:</span>415 206 3791</span>
        <span><span class="label">e:</span>lorajanebecket@meadowpost.net</span>
      </div>
      <div class="contact-row"><span class="label">w:</span>www.lorabecketmft.com</div>
    </div>
  </section>
</body>
</html>
```